今回はコーポレートサイトのTOPページのデザインをお願いしたく思います。

【素材】
素材に関しては、ロゴや写真等は現在準備中でして、
デザインの際は仮のオブジェクトを入れて対応して頂ければと思います。

【サイト構成】
サイトの構成については、ラフを書きましたので下記URLからダウンロードお願いします。
http://qvn.jp/PbLwoR

※PCを想定したデザインでお願いいたします。

【イメージ】
以下が現在の「アオバエステート株式会社」のコーポレートサイトになります。
http://www.aoba-estate.co.jp/

今回ご提案いただく新しいサイトのデザインは上記のものから一新して

1.スタイリッシュ
2.NY
3.最先端
4.近未来
5.エネルギッシュ
6.エキサイティング
7.自由
8.それでいてシンプル

なイメージ、従来の不動産会社のイメージに囚われないものにしたく思います。

【参考サイト】
https://www.kumonomi.co.jp/

1ページ
グレー系
今回のデザインで採用させて頂いた方には、
コーポレートサイトの「代表メッセージ」「ニュース」「投資実績」の他3ページのデザインやコーディングなど、他のお仕事に関してもご相談させて頂ければと思います。
(もちろん当案件のみご希望の方からも募集しており、採用有無には関係ありません。)

色のコンセプトと対応の早さ、デザインの良さで決定致しました。

皆さま、お忙しい所多くのご提案を頂きまして誠にありがとうございます。
また何かございましたらお願いをさせて頂きますので引き続き宜しくお願い致します。

```html
<!DOCTYPE html>
<html lang="ja">
<head>
<meta charset="utf-8">
<title>AOBA ESTATE</title>
<link href="https://fonts.googleapis.com/css2?family=Red+Hat+Display:wght@400;500&family=Noto+Sans+JP:wght@400;500&display=swap" rel="stylesheet">
<style>
:root{
  --bg:#ffffff;
  --panel:#f1f1f1;
  --ink:#3c3f44;
  --muted:#8a8d92;
  --accent:#4ea6d8;
  --footer:#4a4d52;
  --footer-ink:#e8e9ea;
  --footer-muted:#a7aaae;
}
*{margin:0;padding:0;box-sizing:border-box}
html,body{width:1200px;height:2876px;overflow:hidden;background:var(--bg)}
body{position:relative;font-family:"Noto Sans JP","Red Hat Display",sans-serif;color:var(--ink)}
.abs{position:absolute}
.nav{left:96px;top:72px;display:flex;gap:56px;font-family:"Red Hat Display",sans-serif;font-size:15px;color:var(--muted)}
.hero-panel{left:720px;top:200px;width:480px;height:540px;background:var(--panel)}
.hero-photo{left:620px;top:0;width:410px;height:645px;background:linear-gradient(180deg,#3d86c8 0%,#8ec0e8 45%,#e9eef2 46%,#d7dde2 100%)}
.logo{font-family:"Red Hat Display",sans-serif;font-weight:500;font-size:22px;letter-spacing:8px;color:var(--ink)}
.hero-logo{left:96px;top:214px}
.headline{left:86px;top:384px;font-family:"Red Hat Display",sans-serif;font-weight:400;font-size:61px;line-height:64px;color:var(--accent);letter-spacing:-0.5px}
.hero-sub{left:96px;top:700px;font-size:13px;line-height:30px;color:var(--ink);letter-spacing:1px}
.vlabel{font-family:"Red Hat Display",sans-serif;font-size:26px;transform:rotate(-90deg);transform-origin:left top;white-space:nowrap}
.work-label{left:38px;top:966px;color:var(--ink)}
.work-img{top:885px;height:350px}
.w1{left:95px;width:350px;background:linear-gradient(180deg,#7cb4e0 0%,#a9cfe9 35%,#3d3a34 60%,#2f3e2c 100%)}
.w2{left:490px;width:350px;background:linear-gradient(135deg,#8a5d45 0%,#5f6a73 50%,#a7b8c6 100%)}
.w3{left:885px;width:315px;background:linear-gradient(160deg,#6d7780 0%,#3f4a52 55%,#2a2f33 100%)}
.more{left:1030px;top:1035px;font-family:"Red Hat Display",sans-serif;font-size:14px;color:#fff}
.more-line{left:1030px;top:1058px;width:62px;height:1px;background:#fff}
.info-photo{left:0;top:1400px;width:450px;height:630px;background:linear-gradient(180deg,#6fa8d6 0%,#b6d3ea 55%,#a26a48 56%,#7a4a30 100%)}
.info-label{left:34px;top:1600px;color:#fff}
.info-panel{left:450px;top:1600px;width:750px;height:570px;background:var(--panel)}
.info-col{top:1682px;font-size:13px;line-height:21px}
.info-col dt{color:var(--ink);font-weight:500}
.info-col dd{color:var(--muted);margin-bottom:24px}
.col-a{left:590px;width:220px}
.col-b{left:840px;width:260px}
footer{position:absolute;left:0;top:2400px;width:1200px;height:476px;background:var(--footer);color:var(--footer-ink)}
.f-logo{left:130px;top:126px;color:var(--footer-ink)}
.f-head{font-family:"Red Hat Display",sans-serif;font-size:26px;color:#fff}
.news-head{left:408px;top:76px}
.news-list{left:408px;top:132px;list-style:none;font-size:13px;line-height:40px;color:var(--footer-ink)}
.news-list span{display:inline-block;width:110px;font-family:"Red Hat Display",sans-serif;color:var(--footer-muted)}
.addr-head{left:842px;top:76px}
.addr{left:842px;top:130px;font-size:13px;line-height:21px;color:var(--footer-ink)}
.addr .map{margin-left:8px;color:var(--footer-muted)}
.f-rule{left:130px;top:318px;width:940px;height:1px;background:#6a6d72}
.f-nav{left:800px;top:336px;display:flex;gap:38px;font-family:"Red Hat Display",sans-serif;font-size:14px;color:var(--footer-muted)}
.copy{right:130px;top:386px;font-family:"Red Hat Display",sans-serif;font-size:11px;color:var(--footer-muted)}
</style>
</head>
<body>
<nav class="abs nav"><span>About</span><span>Work</span><span>News</span><span>Contact</span></nav>

<div class="abs hero-panel"></div>
<div class="abs hero-photo" role="img" aria-label="Modern white building with a grid of windows against a blue sky"></div>
<div class="abs logo hero-logo">AOBA ESTATE</div>
<h1 class="abs headline">Discover new ways of<br>real estate,<br>Creating a new future<br>for real estate</h1>
<p class="abs hero-sub">不動産の新しい在り方を発見し、<br>不動産の新しい未来を創造する</p>

<div class="abs vlabel work-label">Work</div>
<div class="abs work-img w1" role="img" aria-label="Glass-fronted modern house lit at dusk"></div>
<div class="abs work-img w2" role="img" aria-label="Apartment building facade with balconies"></div>
<div class="abs work-img w3" role="img" aria-label="Dark brick residential building"></div>
<div class="abs more">More</div>
<div class="abs more-line"></div>

<div class="abs info-photo" role="img" aria-label="High-rise tower seen from below with an airplane in the sky"></div>
<div class="abs vlabel info-label">Information</div>
<div class="abs info-panel"></div>

<dl class="abs info-col col-a">
  <dt>会社名称</dt><dd>アオバエステート株式会社</dd>
  <dt>所在地</dt><dd>〒150-0012<br>東京都渋谷区広尾4-8-21<br>グリーンテラス広尾410</dd>
  <dt>TEL</dt><dd>03-5412-7730</dd>
  <dt>FAX</dt><dd>03-5412-7731</dd>
  <dt>代表者</dt><dd>青葉 誠司</dd>
  <dt>従業員</dt><dd>8名</dd>
</dl>
<dl class="abs info-col col-b">
  <dt>創業</dt><dd>1979年2月1日</dd>
  <dt>設立</dt><dd>1980年2月1日</dd>
  <dt>事業内容</dt><dd>土地付建売住宅の建築販売、<br>中古住宅・一般建築、宅地</dd>
  <dt>資格・工事業許可</dt><dd>土地建物賃貸業務<br>建築総合監理業務</dd>
  <dt>取引先金融機関</dt><dd>みなと中央銀行<br>青空信用金庫<br>東都共栄銀行</dd>
</dl>

<footer>
  <div class="abs logo f-logo">AOBA ESTATE</div>
  <div class="abs f-head news-head">News</div>
  <ul class="abs news-list">
    <li><span>2019.10.01</span>社名およびコーポレートサイトを…</li>
    <li><span>2019.09.10</span>【夏季休暇のお知らせ】日頃より…</li>
    <li><span>2019.07.31</span>売却物件を募集中です。詳細は…</li>
  </ul>
  <div class="abs f-head addr-head">Address</div>
  <p class="abs addr">〒150-0012<br>東京都渋谷区広尾4-8-21<br>グリーンテラス広尾410<span class="map">MAP</span></p>
  <div class="abs f-rule"></div>
  <nav class="abs f-nav"><span>About</span><span>Work</span><span>News</span><span>Contact</span></nav>
  <p class="abs copy">© AOBA ESTATE</p>
</footer>
</body>
</html>
```